Vantrelle Greeting Card Desig

I''m seeking a design for a standard size greeting card that will be blank inside and used to say thank you or other messages to customers. It should be in keeping with our corporate image - see website www.vantrelle.com.au The design should incorporate our pen logo and/or abide by colours etc in our style guide.  The look and feel should be clean, fresh, approachable and professional.

Happy for the design to use the pen logo without the words. I will load a version without the text
Size of card - standard greeting card of 11.7cm x 16.6cm (can be either orientation)

Target Market(s)

18+ Years Old

Requirements
Must have
• our logo
• corporate colours

```html
<!DOCTYPE html>
<html lang="en">
<head>
<meta charset="utf-8">
<title>Vantrelle Greeting Card</title>
<link href="https://fonts.googleapis.com/css2?family=Caveat:wght@500;700&family=Permanent+Marker&display=swap" rel="stylesheet">
<style>
  :root {
    --paper: #ffffff;
    --ink: #000000;
    --brand-yellow: #dcdc55;
    --pale-yellow: #f4f6d8;
    --mist-grey: #dcdfe1;
    --panel-line: #e4ecbd;
  }
  * { margin: 0; padding: 0; box-sizing: border-box; }
  html, body {
    width: 804px; height: 1200px; overflow: hidden;
    background: var(--paper);
  }
  .canvas { position: relative; width: 804px; height: 1200px; }
  .panel {
    position: absolute; left: 5px; width: 797px;
    border: 1px solid var(--panel-line);
    background: var(--paper);
    overflow: hidden;
  }
  .panel--front { top: 11px; height: 562px; }
  .panel--back { top: 627px; height: 562px; }

  .brand-mark {
    position: absolute; display: flex; align-items: center; gap: 8px;
    font-family: "Caveat", cursive; font-weight: 700;
  }
  .brand-mark__square { display: block; flex: none; }
  .panel--front .brand-mark { left: 66px; top: 230px; font-size: 30px; color: var(--ink); }
  .panel--front .brand-mark__square { width: 22px; height: 22px; background: var(--brand-yellow); }
  .panel--back .brand-mark { left: 30px; top: 190px; font-size: 96px; color: var(--mist-grey); gap: 14px; }
  .panel--back .brand-mark__square { width: 70px; height: 70px; background: var(--pale-yellow); }

  .field-label {
    position: absolute; right: 405px;
    font-family: "Permanent Marker", cursive;
    font-size: 56px; line-height: 1; color: var(--ink);
  }
  .field-label--to { top: 172px; }
  .field-label--from { top: 292px; }
  .field-line { position: absolute; left: 416px; }
  .field-line--to { top: 229px; }
  .field-line--from { top: 342px; }

  .contact {
    position: absolute; left: 0; right: 0; bottom: 14px;
    text-align: center;
    font-family: "Caveat", cursive; font-weight: 500;
    font-size: 21px; line-height: 19px; color: var(--ink);
  }
</style>
</head>
<body>
<main class="canvas">
  <section class="panel panel--front" aria-label="Card front">
    <div class="brand-mark"><span class="brand-mark__square"></span>Vantrelle</div>

    <span class="field-label field-label--to">To:</span>
    <svg class="field-line field-line--to" width="292" height="16" viewBox="0 0 292 16" aria-hidden="true">
      <path d="M2 10 L6 6 L60 5 L120 3 L180 2 L240 3 L272 5 L290 6 L272 9 L240 9 L180 10 L120 11 L60 12 L12 14 Z" fill="var(--brand-yellow)"/>
    </svg>

    <span class="field-label field-label--from">From:</span>
    <svg class="field-line field-line--from" width="292" height="16" viewBox="0 0 292 16" aria-hidden="true">
      <path d="M2 10 L6 6 L60 5 L120 3 L180 2 L240 3 L272 5 L290 6 L272 9 L240 9 L180 10 L120 11 L60 12 L12 14 Z" fill="var(--brand-yellow)"/>
    </svg>
  </section>

  <section class="panel panel--back" aria-label="Card back">
    <div class="brand-mark"><span class="brand-mark__square"></span>Vantrelle</div>
    <p class="contact">
      Suite 12 48 Harbour Lane Eastwick NSW 2099<br>
      Telephone 02 5550 1234 - www.vantrelle.com.au
    </p>
  </section>
</main>
</body>
</html>
```